electrical contractor business card for professional modern company

I need a business card design for an electrical contractors business. I do all kinds of electricical work from new homes, air conditioning, data and communications. I have a logo design i want on it and have a good idea in my head of what i want it to look like. I like simple yet bold and professional looking. All black background is a must

Target Market(s)

Anyone needing electrical work done

Industry/Entity Type

Electrical

Contact Information for Business Card

company name- KTW Electrical and Data
person name-martin pellowe
phone number- 0418 362 927
website-ktwelec.example.com.au

Font styles to use
Sans Serif

Requirements
Must have
• email
• website
• logo
• name
• phone number
• list of work i do:
• -electrical
• -air-conditioning
• -data/communications
• -cctv/security
• -domestic/commercial/industrial
• -24hr emergency breakdown repair
Nice to have
• i would like the logo on the front side in the centre taking up most of the card with black background.
• on the rear i want the list of work i do with company info i.e. email, website, my name, phone number. rear of card also black background with orange writing to match the orange in the logo

```html
<!DOCTYPE html>
<html lang="en">
<head>
<meta charset="utf-8">
<title>KTW Electrical and Data – Business Card</title>
<link href="https://fonts.googleapis.com/css2?family=Arimo:wght@400;700&display=swap" rel="stylesheet">
<style>
  :root {
    --backdrop: #161616;
    --card-black: #0d0d0d;
    --card-charcoal: #262626;
    --card-edge: #333333;
    --brand-orange: #f26a2e;
    --muted-orange: #e8622a;
  }
  * { box-sizing: border-box; margin: 0; padding: 0; }
  html, body {
    width: 1200px;
    height: 1000px;
    overflow: hidden;
    background: var(--backdrop);
    font-family: "Arimo", Arial, sans-serif;
  }
  .stage {
    width: 1200px;
    height: 1000px;
    display: flex;
    flex-direction: column;
    align-items: center;
    justify-content: center;
    gap: 60px;
  }
  .card {
    width: 700px;
    height: 400px;
    border: 1px solid var(--card-edge);
    position: relative;
  }
  /* Front side */
  .card--front {
    background: linear-gradient(160deg, #1a1a1a 0%, var(--card-black) 55%, #050505 100%);
    display: flex;
    align-items: center;
    justify-content: center;
  }
  .brand {
    display: flex;
    align-items: center;
    gap: 18px;
    color: var(--brand-orange);
    font-weight: 700;
  }
  .brand__mark {
    width: 30px;
    height: 30px;
    border-radius: 50%;
    background: var(--brand-orange);
    flex: none;
  }
  .brand--large .brand__name { font-size: 44px; letter-spacing: 1px; }
  .brand--small { gap: 8px; }
  .brand--small .brand__mark { width: 12px; height: 12px; }
  .brand--small .brand__name { font-size: 17px; }

  /* Back side */
  .card--back {
    background: linear-gradient(170deg, #2e2e2e 0%, var(--card-charcoal) 45%, #161616 100%);
    color: var(--brand-orange);
    padding: 46px 48px 40px;
  }
  .card--back .brand {
    position: absolute;
    top: 46px;
    left: 50%;
    transform: translateX(-50%);
    white-space: nowrap;
  }
  .holder {
    position: absolute;
    left: 48px;
    top: 128px;
  }
  .holder__name { font-size: 22px; font-weight: 700; }
  .holder__role { font-size: 16px; margin-top: 4px; }
  .contact {
    position: absolute;
    left: 48px;
    top: 236px;
    list-style: none;
    font-size: 16px;
    line-height: 22px;
  }
  .services {
    position: absolute;
    left: 392px;
    top: 160px;
    list-style: none;
    font-size: 16px;
    line-height: 22px;
  }
  .services li { display: flex; align-items: center; gap: 8px; white-space: nowrap; }
  .services svg { flex: none; }
</style>
</head>
<body>
<main class="stage">

  <section class="card card--front" aria-label="Business card front">
    <div class="brand brand--large">
      <span class="brand__mark" aria-hidden="true"></span>
      <span class="brand__name">KTW Electrical and Data</span>
    </div>
  </section>

  <section class="card card--back" aria-label="Business card back">
    <div class="brand brand--small">
      <span class="brand__mark" aria-hidden="true"></span>
      <span class="brand__name">KTW Electrical and Data</span>
    </div>

    <div class="holder">
      <p class="holder__name">Martin Pellowe</p>
      <p class="holder__role">Your Designation</p>
    </div>

    <ul class="contact">
      <li>P: 0418 362 927</li>
      <li>E: martinpellowe@ktwelec.example.com.au</li>
      <li>W: ktwelec.example.com.au</li>
    </ul>

    <ul class="services">
      <li><svg width="16" height="6" viewBox="0 0 16 6" aria-hidden="true"><rect x="0" y="1.5" width="10" height="3" rx="1" fill="var(--brand-orange)"/><rect x="10" y="2.4" width="6" height="1.2" fill="var(--brand-orange)"/></svg>electrical</li>
      <li><svg width="16" height="6" viewBox="0 0 16 6" aria-hidden="true"><rect x="0" y="1.5" width="10" height="3" rx="1" fill="var(--brand-orange)"/><rect x="10" y="2.4" width="6" height="1.2" fill="var(--brand-orange)"/></svg>air-conditioning</li>
      <li><svg width="16" height="6" viewBox="0 0 16 6" aria-hidden="true"><rect x="0" y="1.5" width="10" height="3" rx="1" fill="var(--brand-orange)"/><rect x="10" y="2.4" width="6" height="1.2" fill="var(--brand-orange)"/></svg>cctv/security</li>
      <li><svg width="16" height="6" viewBox="0 0 16 6" aria-hidden="true"><rect x="0" y="1.5" width="10" height="3" rx="1" fill="var(--brand-orange)"/><rect x="10" y="2.4" width="6" height="1.2" fill="var(--brand-orange)"/></svg>data/communications</li>
      <li><svg width="16" height="6" viewBox="0 0 16 6" aria-hidden="true"><rect x="0" y="1.5" width="10" height="3" rx="1" fill="var(--brand-orange)"/><rect x="10" y="2.4" width="6" height="1.2" fill="var(--brand-orange)"/></svg>domestic/commercial/industrial</li>
      <li><svg width="16" height="6" viewBox="0 0 16 6" aria-hidden="true"><rect x="0" y="1.5" width="10" height="3" rx="1" fill="var(--brand-orange)"/><rect x="10" y="2.4" width="6" height="1.2" fill="var(--brand-orange)"/></svg>24hr emergency breakdown repair</li>
    </ul>
  </section>

</main>
</body>
</html>
```